STAND UP POUCH Package Artwork
Also a $300 bonus may also apply if stellar and timely and save us money on plates / cylinders.
This project is for retail nutritional products in stand up pouches zipper resealable pouches.
This project is for experienced designers for 2 different products in a line that are already in commerce. We want to keep our company branding logo the same, but want to completely redo the look of these two products. if selected for shortlist we will provide a look at what it is now and it needs to be a complete departure from that. Since we are switching from bottles to pouches this is a great time for a complete departure. Art work will be placed on metalized stand up resealable pouches. Knowledge of cylinder use for artwork (these are like plates and are very expensive so would like to hold to no more then 4 cylinders) Therefore creativity with color is paramount. Any and all question will be welcomed and responded to. This is a GO project so selection will be speedy so show us your best stuff when responding. Must be done in all original artwork.
The look for this project is as follows:
1. Elegant look, timeless, minimal colors optimal impact, strong branding, recognizable by site on shelves, clean lines.
DETAILS
1. Please provide samples of your work pertaining to package design and if on pouches even better.
2. Responses to our posting. Generic responses will be ignored, another words, no spam.
3. The artist(s) that are selected for drafts will be provided with further details on the project.
4. Product A: will be on a 191mm x 267mm x 102mm stand up pouch with gusset bottom. This is a single product with two flavors, Chocolate and vanilla. So when designing for this one think of a way to have minimal cylinder changes. This is a high end nutritional vegan shake type product.
5. Product B: will be on a 127mm x 203mm x76mm stand up pouch with gusset bottom. This is a high end weightless type product.
6. Printing templates will be provided for reference, pouch images will be available to see color options of pouches, tag lines, nutritional facts panel, etc…
Some possible elements will be available on our drop box also.
74% female 34-60 36% male 34-60
Retail

```html
<!DOCTYPE html>
<html lang="en">
<head>
<meta charset="utf-8">
<title>Veralune Shake Pouches</title>
<link rel="stylesheet" href="https://fonts.googleapis.com/css2?family=Tinos&display=swap">
<style>
  :root {
    --page: #ffffff;
    --night: #231f20;
    --leaf: #8bc541;
    --vanilla: #ffffff;
    --cocoa: #7d5200;
    --ink: #231f20;
    --light-text: #ffffff;
    --serif: "Tinos", "Times New Roman", serif;
  }
  * { margin: 0; padding: 0; box-sizing: border-box; }
  html, body { width: 1200px; height: 949px; overflow: hidden; background: var(--page); }
  .stage { position: relative; width: 1200px; height: 949px; }
  .pouch {
    position: absolute;
    top: 135px;
    width: 428px;
    height: 678px;
    box-shadow: 3px 5px 8px rgba(0,0,0,0.35);
    overflow: hidden;
  }
  .pouch--vanilla { left: 140px; }
  .pouch--chocolate { left: 619px; }
  .pouch__art { position: absolute; inset: 0; display: block; }
  .fill-night { fill: var(--night); }
  .fill-leaf { fill: var(--leaf); }
  .fill-vanilla { fill: var(--vanilla); }
  .fill-cocoa { fill: var(--cocoa); }
  .pouch__brand {
    position: absolute;
    top: 152px;
    left: 0;
    width: 100%;
    text-align: center;
    font-family: var(--serif);
    font-size: 34px;
    letter-spacing: 3px;
    color: var(--light-text);
  }
  .pouch__flavor {
    position: absolute;
    top: 572px;
    left: 70px;
    font-family: var(--serif);
    font-size: 26px;
    letter-spacing: 0.5px;
  }
  .pouch--vanilla .pouch__flavor { color: var(--ink); }
  .pouch--chocolate .pouch__flavor { color: var(--light-text); }
</style>
</head>
<body>
<main class="stage">
  <section class="pouch pouch--vanilla">
    <svg class="pouch__art" viewBox="0 0 428 678" width="428" height="678" aria-hidden="true">
      <defs>
        <filter id="wave-shadow-v" x="-10%" y="-10%" width="120%" height="120%">
          <feDropShadow dx="0" dy="-3" stdDeviation="3" flood-color="#000" flood-opacity="0.35"/>
        </filter>
      </defs>
      <rect class="fill-leaf" width="428" height="678"/>
      <path class="fill-night" d="M0,0 H428 V377 C400,385 370,386 340,382 C200,365 80,270 0,183 Z"/>
      <path class="fill-vanilla" filter="url(#wave-shadow-v)" d="M0,506 C40,496 90,490 140,500 C250,525 350,600 405,678 H0 Z"/>
    </svg>
    <p class="pouch__brand">VERALUNE</p>
    <p class="pouch__flavor">VANILLA</p>
  </section>

  <section class="pouch pouch--chocolate">
    <svg class="pouch__art" viewBox="0 0 428 678" width="428" height="678" aria-hidden="true">
      <defs>
        <filter id="wave-shadow-c" x="-10%" y="-10%" width="120%" height="120%">
          <feDropShadow dx="0" dy="-3" stdDeviation="3" flood-color="#000" flood-opacity="0.35"/>
        </filter>
      </defs>
      <rect class="fill-leaf" width="428" height="678"/>
      <path class="fill-night" d="M0,0 H428 V377 C400,385 370,386 340,382 C200,365 80,270 0,183 Z"/>
      <path class="fill-cocoa" filter="url(#wave-shadow-c)" d="M0,506 C40,496 90,490 140,500 C250,525 350,600 405,678 H0 Z"/>
    </svg>
    <p class="pouch__brand">VERALUNE</p>
    <p class="pouch__flavor">CHOCOLATE</p>
  </section>
</main>
</body>
</html>
```